We do the same thing as http://quarrytrades.com. We are called harborbets.com. Need a fast loading website which targets the same demographics as quarrytrades.com. That means a website that is full of energy and excitement, capture concepts of volcano, explosiveness and profit.

Use all content from their site as placeholder.

```html
<!DOCTYPE html>
<html lang="en">
<head>
<meta charset="utf-8">
<title>Harbor Bets – Free Penny Stock Alerts</title>
<link rel="stylesheet" href="https://fonts.googleapis.com/css2?family=Roboto+Condensed:wght@400;700&family=Roboto:wght@400;900&display=swap">
<style>
  :root{
    --black:#000;
    --panel:#0d0d0d;
    --panel-low:#2b2b2b;
    --gold:#d9a41e;
    --gold-line:#c9a02a;
    --white:#f4f4f4;
    --red:#e8241a;
    --orange-top:#f4671f;
    --orange-bottom:#c8160b;
    --blue:#2ab0d8;
    --blue-dark:#0d6f93;
    --button-text:#0b4a63;
    --stripe:#4a4a4a;
  }
  *{box-sizing:border-box;margin:0;padding:0}
  html,body{width:1200px;height:1000px;overflow:hidden;background:var(--black)}
  body{position:relative;font-family:"Roboto Condensed",Arial,sans-serif;color:var(--white)}
  .fire-backdrop{position:absolute;left:0;top:40px;width:1200px;height:400px;
    background:
      radial-gradient(ellipse 60% 70% at 50% 0%,#ff7a1a 0%,#e5320d 30%,rgba(120,10,10,.8) 60%,rgba(0,0,0,0) 100%),
      linear-gradient(#f05a12 0%,#b8160c 35%,#4a0606 70%,#000 100%);}
  .panel{position:absolute;left:143px;top:240px;width:908px;height:760px;background:var(--panel);
    border-left:2px solid var(--gold-line);border-right:2px solid var(--gold-line)}
  .panel-low{position:absolute;left:145px;top:702px;width:904px;height:298px;background:var(--panel-low)}
  .hero-art{position:absolute;left:0;top:0;width:1200px;height:320px}
  .brand{position:absolute;left:130px;top:150px;width:300px;text-align:center;
    font-family:"Roboto Condensed",sans-serif;font-weight:700;font-size:54px;line-height:1;color:var(--gold);letter-spacing:2px}
  .headline{position:absolute;left:175px;top:355px;font-weight:700;font-size:49px;line-height:1;color:var(--gold);letter-spacing:.5px;white-space:nowrap}
  .headline .free{color:var(--white)}
  .perks{position:absolute;left:175px;top:436px;width:860px;height:100px;list-style:none}
  .perk{position:absolute;top:0;display:flex;gap:8px;font-weight:700;font-size:19.5px;line-height:30px;color:var(--white)}
  .perk svg{flex:none;margin-top:4px}
  .perk em{color:var(--red);font-style:italic}
  .perk:nth-child(1){left:0;width:260px}
  .perk:nth-child(2){left:294px;width:260px}
  .perk:nth-child(3){left:606px;width:260px}
  .stripes{position:absolute;left:145px;width:904px;height:7px;
    background:repeating-linear-gradient(90deg,var(--stripe) 0 20px,#2a2a2a 20px 34px)}
  .signup{position:absolute;left:125px;top:585px;width:944px;height:117px;
    background:linear-gradient(var(--orange-top),var(--orange-bottom));box-shadow:0 4px 6px rgba(0,0,0,.5)}
  .signup input{position:absolute;left:52px;top:34px;width:648px;height:48px;border:1px solid #ccc;border-radius:7px;
    background:#fff;padding:0 16px;font-family:"Roboto Condensed",sans-serif;font-size:25px;color:#666}
  .signup input::placeholder{color:#777}
  .signup button{position:absolute;left:711px;top:34px;width:181px;height:48px;border:1px solid #0d6f93;border-radius:6px;
    background:linear-gradient(#3fc4e8,var(--blue) 55%,var(--blue-dark));font-family:"Roboto Condensed",sans-serif;font-weight:700;font-size:40px;line-height:44px;color:var(--button-text)}
  .wins{position:absolute;left:145px;top:760px;width:904px;height:220px}
  .win{position:absolute;top:0;width:200px;height:220px}
  .win .ring{position:absolute;left:0;top:0;width:200px;height:200px;border-radius:50%;
    background:radial-gradient(circle,rgba(0,0,0,0) 56%,#ffcf4a 60%,#f07a10 68%,rgba(200,40,0,.5) 80%,rgba(0,0,0,0) 92%)}
  .win .core{position:absolute;left:32px;top:46px;width:136px;height:136px;border-radius:50%;background:#070707;text-align:center}
  .win .ticker{display:block;margin-top:30px;font-weight:700;font-size:48px;line-height:1;color:#f2a818}
  .win .gain{display:block;margin-top:6px;font-weight:700;font-size:20px;color:var(--white)}
  .win:nth-child(1){left:40px}.win:nth-child(2){left:252px}.win:nth-child(3){left:464px}.win:nth-child(4){left:676px}
</style>
</head>
<body>
  <div class="fire-backdrop" role="img" aria-label="Glowing flames and red glitter sparks across the top"></div>
  <div class="panel"></div>
  <div class="panel-low"></div>

  <svg class="hero-art" viewBox="0 0 1200 320" aria-hidden="false">
    <defs>
      <linearGradient id="chartFill" x1="0" y1="0" x2="1" y2="1">
        <stop offset="0" stop-color="#0a1c5a"/><stop offset=".5" stop-color="#1636a8"/><stop offset="1" stop-color="#07103a"/>
      </linearGradient>
    </defs>
    <g role="img" aria-label="Blue stock market chart with a rising line">
      <path d="M420 90 L1110 40 Q1100 160 1110 240 Q760 250 420 285 Z" fill="url(#chartFill)" stroke="#d9a41e" stroke-width="3"/>
      <polyline points="470,270 540,240 600,250 660,210 720,190 760,150 820,160 870,120 920,130 970,100 1030,110 1090,95"
        fill="none" stroke="#7fb8ff" stroke-width="2.5"/>
    </g>
    <g class="ribbon">
      <path d="M430 95 L1108 38 L1125 85 L445 135 Z" fill="#fff" stroke="#d9a41e" stroke-width="3"/>
      <text x="475" y="118" transform="rotate(-4.6 475 118)" font-family="Roboto,Arial,sans-serif" font-size="25" fill="#111">RECEIVE <tspan font-weight="900" font-size="31">HOT</tspan> PENNY STOCK <tspan font-weight="900" font-size="31">ALERTS</tspan> FOR <tspan font-weight="900" font-style="italic" font-size="33" fill="#e8241a">FREE!</tspan></text>
    </g>
  </svg>

  <div class="brand">HARBOR<br>BETS</div>

  <h1 class="headline">SIGN UP FOR <span class="free">FREE</span> PENNY STOCK ALERTS!</h1>

  <ul class="perks">
    <li class="perk"><svg width="32" height="26" viewBox="0 0 32 26"><path d="M2 14 L11 23 L30 2 L11 16 Z" fill="#d9a41e"/></svg><span>Join the Most Explosive Penny Stock Newsletter on the WEB ... <em>100% FREE</em></span></li>
    <li class="perk"><svg width="32" height="26" viewBox="0 0 32 26"><path d="M2 14 L11 23 L30 2 L11 16 Z" fill="#d9a41e"/></svg><span>HOT Penny <em>Stock Alerts</em> Delivered Directly to your Email</span></li>
    <li class="perk"><svg width="32" height="26" viewBox="0 0 32 26"><path d="M2 14 L11 23 L30 2 L11 16 Z" fill="#d9a41e"/></svg><span><em>Don't hesitate!</em> There are LIMITED spots available.</span></li>
  </ul>

  <div class="stripes" style="top:578px"></div>
  <form class="signup">
    <input type="email" placeholder="Enter your email address...">
    <button type="button">SIGN UP</button>
  </form>
  <div class="stripes" style="top:702px"></div>

  <div class="wins">
    <div class="win"><div class="ring" role="img" aria-label="Fiery ring"></div><div class="core"><span class="ticker">QRLX</span><span class="gain">840% GAIN</span></div></div>
    <div class="win"><div class="ring" role="img" aria-label="Fiery ring"></div><div class="core"><span class="ticker">NVTR</span><span class="gain">800% GAIN</span></div></div>
    <div class="win"><div class="ring" role="img" aria-label="Fiery ring"></div><div class="core"><span class="ticker">BKRA</span><span class="gain">212% GAIN</span></div></div>
    <div class="win"><div class="ring" role="img" aria-label="Fiery ring"></div><div class="core"><span class="ticker">SHMQ</span><span class="gain">142% GAIN</span></div></div>
  </div>
</body>
</html>
```